Corvane Supplies Business Card

Professional business card that stand out to our potential customers. Front and back with clean modern design

Industry/Entity Type

Oil and gas

Contact Information for Business Card

Name, address, website , office phone and cell number

Requirements
Must have
• Editable files for each employee

```html
<!DOCTYPE html>
<html lang="en">
<head>
<meta charset="utf-8">
<title>Corvane Supplies Business Card</title>
<link rel="stylesheet" href="https://fonts.googleapis.com/css2?family=Open+Sans:wght@400;700&display=swap">
<style>
  :root {
    --cyan: #05b0d0;
    --ink: #000000;
    --paper: #ffffff;
    --backdrop: #ffffff;
  }
  html, body {
    margin: 0;
    padding: 0;
    width: 1100px;
    height: 1200px;
    overflow: hidden;
    background: var(--backdrop);
    font-family: "Open Sans", Arial, sans-serif;
  }
  .card {
    position: absolute;
    left: 116px;
    width: 877px;
    height: 478px;
    background: var(--paper);
    box-shadow: 8px 10px 22px rgba(0, 0, 0, 0.22);
  }
  .card--front { top: 63px; }
  .card--back { top: 668px; }
  .card svg { display: block; width: 100%; height: 100%; }
  .brand-name { font-family: "Open Sans", Arial, sans-serif; font-weight: 700; fill: var(--ink); }
  .brand-mark { fill: var(--cyan); }
  .company-name { font-family: "Open Sans", Arial, sans-serif; font-weight: 400; fill: var(--ink); font-size: 30px; }
  .contact { font-family: "Open Sans", Arial, sans-serif; fill: var(--ink); }
  .icon-dot { fill: var(--cyan); }
  .icon-glyph { fill: none; stroke: var(--paper); stroke-width: 1.4; stroke-linecap: round; stroke-linejoin: round; }
  .rule { stroke: var(--cyan); stroke-width: 1.5; }
</style>
</head>
<body>

<section class="card card--front" aria-label="Card front">
  <svg viewBox="0 0 877 478" xmlns="http://www.w3.org/2000/svg">
    <rect class="brand-mark" x="192" y="224" width="28" height="28"/>
    <text class="brand-name" x="458" y="254" font-size="44" text-anchor="middle">Corvane Supplies</text>
  </svg>
</section>

<section class="card card--back" aria-label="Card back">
  <svg viewBox="0 0 877 478" xmlns="http://www.w3.org/2000/svg">
    <!-- brand -->
    <rect class="brand-mark" x="72" y="216" width="18" height="18"/>
    <text class="brand-name" x="230" y="234" font-size="28" text-anchor="middle">Corvane Supplies</text>

    <!-- divider -->
    <line class="rule" x1="438" y1="119" x2="438" y2="359"/>

    <!-- contact block -->
    <text class="company-name" x="657" y="139" text-anchor="middle">COMPANY NAME</text>

    <line class="rule" x1="544" y1="182" x2="595" y2="182"/>
    <line class="rule" x1="720" y1="182" x2="771" y2="182"/>

    <g class="contact-icons">
      <!-- mobile phone -->
      <circle class="icon-dot" cx="605" cy="182" r="10"/>
      <path class="icon-glyph" d="M601 177 q-1 6 5 10 l2-2 -2-2 -1 1 q-2-2-3-4 l1-1 -2-2z"/>
      <!-- office phone -->
      <circle class="icon-dot" cx="631" cy="182" r="10"/>
      <path class="icon-glyph" d="M625 180 q6-5 12 0 M627 181 h8 l1 5 h-10z"/>
      <!-- location pin -->
      <circle class="icon-dot" cx="658" cy="182" r="10"/>
      <path class="icon-glyph" d="M658 189 q-5-5-5-9 a5 5 0 0 1 10 0 q0 4-5 9z"/>
      <circle cx="658" cy="180" r="1.6" fill="#fff"/>
      <!-- email -->
      <circle class="icon-dot" cx="684" cy="182" r="10"/>
      <path class="icon-glyph" d="M678 178 h12 v8 h-12z M678 178 l6 5 6-5"/>
      <!-- web -->
      <circle class="icon-dot" cx="710" cy="182" r="10"/>
      <circle class="icon-glyph" cx="710" cy="182" r="6"/>
      <path class="icon-glyph" d="M704 182 h12 M710 176 q-4 6 0 12 q4-6 0-12"/>
    </g>

    <text class="contact" x="657" y="235" font-size="22" text-anchor="middle">012 345 6789</text>
    <text class="contact" x="657" y="257" font-size="18" text-anchor="middle">012 345 6789</text>
    <text class="contact" x="657" y="281" font-size="21" text-anchor="middle">addresscityname000</text>
    <text class="contact" x="657" y="308" font-size="17" text-anchor="middle">youremail@corvanemail.com</text>
    <text class="contact" x="657" y="334" font-size="18" text-anchor="middle">www.yourwebsite.com</text>

    <!-- footer bands -->
    <polygon points="0,448 443,448 432,478 0,478" fill="var(--cyan)"/>
    <polygon points="448,448 877,448 877,478 437,478" fill="var(--ink)"/>
  </svg>
</section>

</body>
</html>
```